Business Card Design Project

Business Card
We are rebranding with a new logo
Industry/Entity Type
Business
Contact Information for Business Card
Dennis Marlow +61 427581962 dennis@qovo.com.au P.O. Box 872 Kelvindale QLD 4309
Requirements
Must have
- Logo

```html
<!DOCTYPE html>
<html lang="en">
<head>
<meta charset="utf-8">
<title>Qovo International – Business Card</title>
<link rel="stylesheet" href="https://fonts.googleapis.com/css2?family=Arimo:wght@400;700&display=swap">
<style>
  :root {
    --backdrop: #8f8f8f;
    --card: #ffffff;
    --brand-blue: #1b6fa8;
    --rule-blue: #1a8fd6;
    --swoosh-light: #22a8e0;
    --swoosh-dark: #0d6fae;
    --accent-orange: #f0883a;
    --contact-orange: #f4a064;
  }
  * { margin: 0; padding: 0; box-sizing: border-box; }
  html, body {
    width: 1200px;
    height: 1032px;
    overflow: hidden;
    background: var(--backdrop);
    font-family: "Arimo", Arial, sans-serif;
  }
  .business-card {
    position: absolute;
    left: 100px;
    top: 210px;
    width: 1000px;
    height: 611px;
    background: var(--card);
    overflow: hidden;
  }
  .card-swoosh {
    position: absolute;
    inset: 0;
    width: 1000px;
    height: 611px;
  }
  .brand {
    position: absolute;
    left: 70px;
    top: 170px;
    display: flex;
    align-items: center;
    gap: 18px;
  }
  .brand-dot {
    width: 34px;
    height: 34px;
    border-radius: 50%;
    background: var(--accent-orange);
  }
  .brand-name {
    color: var(--brand-blue);
    font-weight: 700;
    line-height: 1;
  }
  .brand-name .word {
    display: block;
    font-size: 92px;
    letter-spacing: -1px;
  }
  .brand-name .descriptor {
    display: block;
    font-size: 21px;
    letter-spacing: 5px;
    margin-top: 8px;
  }
  .contact {
    position: absolute;
    left: 475px;
    top: 222px;
    right: 0;
  }
  .contact-name {
    color: var(--brand-blue);
    font-size: 46px;
    font-weight: 700;
    padding-bottom: 8px;
    border-bottom: 5px solid var(--rule-blue);
  }
  .contact-details {
    list-style: none;
    margin-top: 12px;
    color: var(--contact-orange);
    font-size: 32px;
    line-height: 40px;
  }
</style>
</head>
<body>
  <main class="business-card">
    <svg class="card-swoosh" viewBox="0 0 1000 611" aria-hidden="true">
      <defs>
        <linearGradient id="swooshBlue" x1="0" y1="1" x2="1" y2="0">
          <stop offset="0" stop-color="var(--swoosh-light)"/>
          <stop offset="1" stop-color="var(--swoosh-dark)"/>
        </linearGradient>
        <linearGradient id="swooshOrange" x1="0" y1="0" x2="1" y2="1">
          <stop offset="0" stop-color="#f6a24a"/>
          <stop offset="1" stop-color="#e4642a"/>
        </linearGradient>
      </defs>
      <path d="M260 611 Q680 560 1000 380 L1000 611 Z" fill="url(#swooshBlue)"/>
      <path d="M1000 440 Q905 505 915 611 L1000 611 Z" fill="url(#swooshOrange)"/>
    </svg>

    <div class="brand">
      <span class="brand-dot"></span>
      <div class="brand-name">
        <span class="word">Qovo</span>
        <span class="descriptor">INTERNATIONAL</span>
      </div>
    </div>

    <section class="contact">
      <h1 class="contact-name">Dennis Marlow</h1>
      <ul class="contact-details">
        <li>Mobile: +61 427581962</li>
        <li>E-mail: dennis@qovo.com.au</li>
        <li>Address: P.O. Box 872</li>
        <li>Kelvindale QLD 4309</li>
      </ul>
    </section>
  </main>
</body>
</html>
```